Front and content page design for Fitness Cookbook

I am looking for someone to Design a front cover for a Recipe book and also create an amazing layout for the book.

Its for a corporate seminar so has to be eye catching, professional and bold.

Content is complete

Target Market(s)

Industry/Entity Type

Health And Wellness

Font styles to use
Sans Serif

Requirements
Must have
• Eye catching, professional and bold.
• By Dorian as stated on the document
• Must have Velmora Athletics Logo on it.

```html
<!DOCTYPE html>
<html lang="en">
<head>
<meta charset="utf-8">
<title>Recipes – Beef Burgers and Baked Salmon</title>
<link href="https://fonts.googleapis.com/css2?family=Oswald:wght@400;500&family=Arimo:ital,wght@0,400;0,700;1,400;1,700&display=swap" rel="stylesheet">
<style>
  :root {
    --page: #ffffff;
    --accent: #f28a2e;
    --accent-text: #ffffff;
    --ink: #2b2b2b;
    --rule: #c9c9c9;
    --photo-burger-a: #6b5a48;
    --photo-burger-b: #b23a3a;
    --photo-burger-c: #4f7a3a;
    --photo-salmon-a: #7a4e7a;
    --photo-salmon-b: #c58a52;
    --photo-salmon-c: #e6e2dc;
  }
  * { box-sizing: border-box; margin: 0; padding: 0; }
  html, body { width: 849px; height: 1200px; overflow: hidden; background: var(--page); }
  .page {
    position: relative;
    width: 849px;
    height: 1200px;
    background: var(--page);
    font-family: "Arimo", Arial, sans-serif;
    color: var(--ink);
    font-size: 13.5px;
    line-height: 1.4;
  }
  .recipe-photo { position: absolute; }
  .recipe-photo--burger {
    left: 66px; top: 36px; width: 350px; height: 330px;
    background: radial-gradient(ellipse at 50% 55%, var(--photo-burger-b) 0%, var(--photo-burger-a) 45%, var(--photo-burger-c) 70%, #d9d5cf 100%);
  }
  .recipe-photo--salmon {
    left: 66px; top: 666px; width: 446px; height: 344px;
    background: linear-gradient(160deg, var(--photo-salmon-a) 0%, var(--photo-salmon-a) 30%, var(--photo-salmon-b) 55%, #8a5a33 75%, var(--photo-salmon-c) 100%);
  }
  .recipe-title {
    position: absolute;
    left: 540px; width: 309px;
    background: var(--accent);
    color: var(--accent-text);
    font-family: "Oswald", "Arial Narrow", sans-serif;
    font-weight: 400;
    font-size: 29px;
    line-height: 1.2;
    padding: 10px 16px;
  }
  .recipe-title--burger { top: 36px; }
  .recipe-title--salmon { top: 666px; }
  .recipe-details { position: absolute; left: 556px; width: 270px; }
  .recipe-details--burger { top: 112px; }
  .recipe-details--salmon { top: 806px; }
  .recipe-details .timing { margin-bottom: 14px; }
  .recipe-details .label { font-style: italic; }
  .ingredient-list { list-style: none; }
  .method { position: absolute; left: 66px; }
  .method--burger { top: 384px; width: 440px; }
  .method--salmon { top: 1028px; width: 460px; }
  .method .label { font-weight: 700; font-style: italic; margin-bottom: 14px; }
  .method p + p { margin-top: 14px; }
  .section-rule {
    position: absolute; left: 66px; right: 0; top: 622px;
    border-top: 1px solid var(--rule);
  }
</style>
</head>
<body>
<main class="page">

  <section class="recipe recipe--burger">
    <div class="recipe-photo recipe-photo--burger" role="img" aria-label="Photo of two beef burger patties topped with spinach and beetroot slices on a plate"></div>
    <h2 class="recipe-title recipe-title--burger">Homemade Beef Burgers</h2>
    <div class="recipe-details recipe-details--burger">
      <div class="timing">
        <p>Prep time: 5 mins</p>
        <p>Cooking time: 20 mins</p>
      </div>
      <p class="label">Ingredients:</p>
      <ul class="ingredient-list">
        <li>Makes 3-4 burgers</li>
        <li>500g grass fed lean beef mince</li>
        <li>1 whole egg</li>
        <li>1 egg white</li>
        <li>Tbsp coconut oil</li>
        <li>½ cup onions</li>
        <li>2 cloves garlic</li>
        <li>2 fresh chillies (optional)</li>
        <li>Salt, pepper, mixed herbs to taste</li>
        <li>2 handful of spinach</li>
        <li>4 slices of beetroot</li>
      </ul>
    </div>
    <div class="method method--burger">
      <p class="label">Cooking Instructions:</p>
      <p>Mash the egg and egg white into the mince and add the onions, garlic, chillies and spices in the same bowl. Use your hands to mould the mixture into 3-4 patties. Fry the patties in the coconut oil on a medium heat, turning throughout till cooked. Layer the spinach and beetroot on top of each one.</p>
    </div>
  </section>

  <hr class="section-rule">

  <section class="recipe recipe--salmon">
    <div class="recipe-photo recipe-photo--salmon" role="img" aria-label="Photo of a herb-crusted baked salmon fillet beside sautéed red cabbage on a white plate"></div>
    <h2 class="recipe-title recipe-title--salmon">Baked Salmon and<br>Sautéed Red Cabbage</h2>
    <div class="recipe-details recipe-details--salmon">
      <div class="timing">
        <p>Prep time: 5 mins</p>
        <p>Cooking time: 15 mins</p>
      </div>
      <p class="label">Ingredients:</p>
      <ul class="ingredient-list">
        <li>200g Salmon fillet</li>
        <li>Optional seasoning for salmon:</li>
        <li>Salt, pepper, mixed herbs and chilli flakes</li>
        <li>1 tsp coconut oil or grass fed butter</li>
        <li>1 cup red cabbage</li>
        <li>¼ white onion</li>
        <li>1 fresh red chilli</li>
      </ul>
    </div>
    <div class="method method--salmon">
      <p class="label">Cooking Instructions:</p>
      <p>Season salmon and bake in the oven for 12-15 minutes at 180°C/374°F</p>
      <p>Whilst cooking melt the coconut oil/butter in the pan, add the red cabbage and saute for 3-4 minutes. Add the onion and chopped up red chilli and continue to cook and mix till onion and cabbage starts to brown. Serve beside salmon.</p>
    </div>
  </section>

</main>
</body>
</html>
```